Tree Service Billboard 20x8 ft

We need a billboard design for a tree service company.
The billboard is 20ft x 8 ft so we need a design that is capable to stretching to those dimensions without loosing quality.
I have attached a series of images.
Image 1- Simply a billboard that I think looks good that I would like you to use for inspiration. I am aiming for the same format only no color in the wording, just black white, or gray. I like the the trees in the background, the logo placed to the left, and wording on the right.
Image 2- Current Logo I would like to the left of the billboard
Image 3- Another format of current logo if needed.
Image 4- A drawn out design template
Image 5- Another drawn out design template

Specific things I am looking for
-The contact number to be the largest thing on the design
-The logo on the design
-Key points to the design to say:
Tree Removal
Tree Trimming
Land Development
Stump Grinding
Storm Response
Insured
Free Bids
-The facebook logo
-The Google Logo

```html
<!DOCTYPE html>
<html lang="en">
<head>
<meta charset="utf-8">
<title>Birch &amp; Vale Tree Care — Billboard</title>
<link rel="stylesheet" href="https://fonts.googleapis.com/css2?family=Chakra+Petch:wght@600&family=Lexend:wght@400;600&display=swap">
<style>
  :root {
    --backdrop: #8c8c8c;
    --olive: #4b4a21;
    --white: #ffffff;
    --sky-light: #f3e3b0;
    --sky-haze: #c9c49a;
    --foliage: #7c9a3c;
    --meadow: #5e7a2c;
    --canopy: #34401c;
    --trunk: #4a4228;
  }
  * { margin: 0; padding: 0; box-sizing: border-box; }
  html, body {
    width: 1200px;
    height: 1200px;
    overflow: hidden;
    background: var(--backdrop);
  }
  .billboard {
    position: absolute;
    left: 62px;
    top: 385px;
    width: 1076px;
    height: 430px;
    background: var(--olive);
    overflow: hidden;
    box-shadow: 0 2px 6px rgba(0, 0, 0, 0.25);
  }
  .billboard-shapes {
    position: absolute;
    inset: 0;
    width: 100%;
    height: 100%;
  }
  .brand {
    position: absolute;
    left: 877px;
    top: 46px;
    transform: translateX(-50%);
    display: flex;
    flex-direction: column;
    align-items: center;
    color: var(--white);
    font-family: "Lexend", sans-serif;
  }
  .brand-mark {
    width: 79px;
    height: 79px;
    border: 3px solid var(--white);
    border-radius: 50%;
    background: rgba(255, 255, 255, 0.14);
  }
  .brand-name {
    margin-top: 14px;
    font-weight: 600;
    font-size: 18px;
    line-height: 22px;
    white-space: nowrap;
  }
  .brand-phone {
    margin-top: 3px;
    display: flex;
    align-items: center;
    gap: 8px;
    font-weight: 600;
    font-size: 11px;
    letter-spacing: 1px;
  }
  .brand-phone::before,
  .brand-phone::after {
    content: "";
    width: 44px;
    height: 1.5px;
    background: var(--white);
  }
  .phone-number {
    position: absolute;
    left: 826px;
    top: 243px;
    transform: translate(-50%, -50%);
    font-family: "Chakra Petch", sans-serif;
    font-weight: 600;
    font-size: 52px;
    letter-spacing: 3px;
    color: var(--olive);
    white-space: nowrap;
  }
  .services {
    position: absolute;
    right: 86px;
    top: 304px;
    list-style: none;
    text-align: right;
    font-family: "Lexend", sans-serif;
    font-weight: 400;
    font-size: 22px;
    line-height: 28.5px;
    letter-spacing: 0.3px;
    color: var(--white);
    white-space: nowrap;
  }
  .social {
    position: absolute;
    left: 38px;
    top: 347px;
    display: flex;
    gap: 19px;
  }
  .social-dot {
    width: 48px;
    height: 48px;
    border: 3px solid var(--white);
    border-radius: 50%;
    background: rgba(255, 255, 255, 0.14);
  }
</style>
</head>
<body>
  <div class="billboard">
    <svg class="billboard-shapes" viewBox="0 0 860 344" preserveAspectRatio="none">
      <defs>
        <linearGradient id="scene-tone" x1="0" y1="0" x2="0" y2="1">
          <stop offset="0" stop-color="var(--canopy)"/>
          <stop offset="0.28" stop-color="var(--meadow)"/>
          <stop offset="0.46" stop-color="var(--sky-haze)"/>
          <stop offset="0.56" stop-color="var(--sky-light)"/>
          <stop offset="0.66" stop-color="var(--foliage)"/>
          <stop offset="0.82" stop-color="var(--meadow)"/>
          <stop offset="1" stop-color="var(--canopy)"/>
        </linearGradient>
        <radialGradient id="scene-glow" cx="0.3" cy="0.5" r="0.45">
          <stop offset="0" stop-color="var(--sky-light)" stop-opacity="0.9"/>
          <stop offset="1" stop-color="var(--sky-light)" stop-opacity="0"/>
        </radialGradient>
        <linearGradient id="scene-shade" x1="0" y1="0" x2="1" y2="0">
          <stop offset="0.4" stop-color="var(--trunk)" stop-opacity="0"/>
          <stop offset="0.62" stop-color="var(--trunk)" stop-opacity="0.45"/>
          <stop offset="0.85" stop-color="var(--trunk)" stop-opacity="0"/>
        </linearGradient>
      </defs>
      <g role="img" aria-label="Photo of a large old tree in a green landscape at sunrise">
        <path class="scene-photo" d="M155,0 L570,0 L351,344 L175,344 C110,300 82,230 85,160 C88,95 115,40 155,0 Z" fill="url(#scene-tone)"/>
        <path class="scene-photo-glow" d="M155,0 L570,0 L351,344 L175,344 C110,300 82,230 85,160 C88,95 115,40 155,0 Z" fill="url(#scene-glow)"/>
        <path class="scene-photo-shade" d="M155,0 L570,0 L351,344 L175,344 C110,300 82,230 85,160 C88,95 115,40 155,0 Z" fill="url(#scene-shade)"/>
      </g>
      <path class="scene-rim" d="M149,3 C112,42 88,96 84,158 C82,200 88,235 100,262" fill="none" stroke="var(--white)" stroke-width="2.5"/>
      <polygon class="phone-band" points="465,165 860,165 860,222 429,222" fill="var(--white)"/>
    </svg>

    <div class="brand">
      <div class="brand-mark"></div>
      <div class="brand-name">BIRCH &amp; VALE TREE CARE</div>
      <div class="brand-phone">555-014-2288</div>
    </div>

    <div class="phone-number">555-014-2288</div>

    <ul class="services">
      <li>Tree Removal • Tree Trimming</li>
      <li>Land Development • Stump Grinding</li>
      <li>Storm Response • Insured • Free Bids</li>
    </ul>

    <div class="social">
      <div class="social-dot"></div>
      <div class="social-dot"></div>
    </div>
  </div>
</body>
</html>
```